Web Developer Needs a Business Card Design

I need a personal business card design that represents me as a web developer for potential employers. I would like the background to be a dark color on the front for contrast with my logo and name. The back will have all my information along with a smaller version of the logo. I want something with a modern look and feel, not too conservative. This will be used for potential employers and freelance work.

Industry/Entity Type

Business

Contact Information for Business Card

Front should have my logo and name. The back should have all my personal information which would include: name: Tom Brevardi, phone: 570-614-9083, email: tombrevardi@mailwisp.com, website url: www.tombrevardi.com, logo, web developer.

Font styles to use
Sans Serif

Requirements
Must have
• Must include my logo. The color palette base color will be the logo color.

```html
<!DOCTYPE html>
<html lang="en">
<head>
<meta charset="utf-8">
<title>Tom Brevardi – Business Card</title>
<link rel="stylesheet" href="https://fonts.googleapis.com/css2?family=Roboto:wght@400;500&display=swap">
<style>
  :root {
    --backdrop: #a8a5a5;
    --teal: #52e2c0;
    --card-dark: #0c0c0c;
    --photo-tone-a: #141414;
    --photo-tone-b: #0a0a0a;
  }
  * { margin: 0; padding: 0; box-sizing: border-box; }
  html, body { width: 1200px; height: 1200px; overflow: hidden; }
  body {
    background: var(--backdrop);
    font-family: "Roboto", Arial, sans-serif;
    position: relative;
  }
  .card {
    position: absolute;
    width: 712px;
    height: 420px;
    border-radius: 30px;
    background: var(--teal);
    padding: 18px;
  }
  .card--front { left: 238px; top: 118px; }
  .card--back { left: 230px; top: 642px; }
  .card__face {
    position: relative;
    width: 100%;
    height: 100%;
    border-radius: 16px;
    background: var(--card-dark);
    overflow: hidden;
  }
  .card__photo {
    position: absolute;
    inset: 0;
    background: radial-gradient(ellipse at 18% 45%, var(--photo-tone-a) 0%, var(--photo-tone-b) 60%),
                linear-gradient(90deg, var(--photo-tone-a), var(--photo-tone-b));
  }
  .mark {
    position: absolute;
    display: flex;
    flex-direction: column;
    align-items: center;
    gap: 18px;
    color: var(--teal);
    font-weight: 500;
  }
  .mark__circle {
    border: 10px solid var(--teal);
    border-radius: 50%;
  }
  .card--front .mark { left: 50%; top: 50%; transform: translate(-50%, -50%); }
  .card--front .mark__circle { width: 140px; height: 140px; }
  .card--front .mark__name { font-size: 34px; }
  .card--back .mark { left: 68px; top: 82px; }
  .card--back .mark__circle { width: 150px; height: 150px; }
  .card--back .mark__name { font-size: 22px; }
  .identity {
    position: absolute;
    left: 355px;
    top: 92px;
    color: var(--teal);
  }
  .identity__name { font-size: 30px; font-weight: 400; letter-spacing: 0.3px; }
  .identity__role { font-size: 17px; margin-top: 10px; }
  .contacts {
    position: absolute;
    left: 355px;
    top: 210px;
    list-style: none;
    color: var(--teal);
    font-size: 19px;
  }
  .contacts li { display: flex; align-items: center; height: 28px; }
  .contacts svg { width: 16px; height: 16px; margin-right: 22px; fill: var(--teal); }
</style>
</head>
<body>
  <section class="card card--front">
    <div class="card__face">
      <div class="card__photo" role="img" aria-label="Dimmed photo of a desk with keyboard and notebook"></div>
      <div class="mark">
        <div class="mark__circle"></div>
        <div class="mark__name">Tom Brevardi</div>
      </div>
    </div>
  </section>

  <section class="card card--back">
    <div class="card__face">
      <div class="card__photo" role="img" aria-label="Dimmed photo of a desk with keyboard and notebook"></div>
      <div class="mark">
        <div class="mark__circle"></div>
        <div class="mark__name">Tom Brevardi</div>
      </div>
      <div class="identity">
        <h1 class="identity__name">Tom Brevardi</h1>
        <p class="identity__role">Web Developer</p>
      </div>
      <ul class="contacts">
        <li>
          <svg viewBox="0 0 16 16" aria-hidden="true"><path d="M1 5c0-2 3-3 7-3s7 1 7 3v1h-4V5H5v1H1z M3 7h10l1 7H2z M8 9a2 2 0 1 0 0.01 0z"/></svg>
          570-614-9083
        </li>
        <li>
          <svg viewBox="0 0 16 16" aria-hidden="true"><path d="M1 3h14v10H1z M2.5 4.5 8 9l5.5-4.5v-.3H2.5z" fill-rule="evenodd"/></svg>
          tombrevardi@mailwisp.com
        </li>
        <li>
          <svg viewBox="0 0 16 16" aria-hidden="true"><circle cx="8" cy="8" r="6.5" fill="none" stroke="#52e2c0" stroke-width="1.4"/><ellipse cx="8" cy="8" rx="2.8" ry="6.5" fill="none" stroke="#52e2c0" stroke-width="1.2"/><path d="M1.5 8h13" stroke="#52e2c0" stroke-width="1.2"/></svg>
          www.tombrevardi.com
        </li>
      </ul>
    </div>
  </section>
</body>
</html>
```